Company service wheel graphic

A graphic demonstrating all the services the company offers.
I have hand drawn and written up on the attached the content that is required. Also attached is our company logo so you have a sense of the colour scheme of the logo.
This will eventually go into a company brochure, be used on our website etc.

Target Market(s)

Local GOvernment and other professionals who work in the sport, recreation and leisure industries

Industry/Entity Type

Sports, recreation, leisure, aquatics

Font styles to use
Other font styles liked:
• Calibri

Colors
0054AA
0677BA
7BADD7
CADEEF
E8F1F8

Requirements
Must have
• An eye catching graphic that captures all the information in the hand drawn atachement.
Nice to have
• Each quadrant in the circle to have its own colour, that links to the company logo

```html
<!DOCTYPE html>
<html lang="en">
<head>
<meta charset="utf-8">
<title>Service Wheel – Community + Stakeholder Engagement</title>
<link href="https://fonts.googleapis.com/css2?family=Arimo:wght@700&family=Righteous&display=swap" rel="stylesheet">
<style>
  :root{
    --bg:#DDEAF5;
    --mid-blue:#0F75BC;
    --navy:#262262;
    --light-blue:#7BADD7;
    --ring-text:#7BAAD6;
    --white:#FFFFFF;
  }
  html,body{margin:0;padding:0;width:1200px;height:1200px;overflow:hidden;background:var(--bg);}
  .wheel{display:block;width:1200px;height:1200px;}
  .service-text{font-family:"Righteous",Calibri,sans-serif;font-size:30px;fill:var(--white);}
  .bullet{fill:var(--white);}
  .ring-label{font-family:"Arimo",Arial,sans-serif;font-weight:700;font-size:72px;fill:var(--ring-text);}
  .ring-dot{fill:var(--ring-text);}
  .pill-text{font-family:"Righteous",Calibri,sans-serif;fill:var(--navy);font-size:40px;}
  .tab-text{font-family:"Righteous",Calibri,sans-serif;fill:var(--white);font-size:24px;}
  .core-text{font-family:"Righteous",Calibri,sans-serif;fill:var(--white);font-size:70px;}
</style>
</head>
<body>
<svg class="wheel" viewBox="0 0 1932 1932" xmlns="http://www.w3.org/2000/svg">
  <defs>
    <clipPath id="disc"><circle cx="966" cy="966" r="731"/></clipPath>
    <path id="arc-top" d="M216,966 A750,750 0 0 1 1716,966"/>
    <path id="arc-bottom" d="M136,966 A830,830 0 0 0 1796,966"/>
  </defs>

  <rect width="1932" height="1932" fill="var(--bg)"/>

  <!-- Outer audience ring -->
  <g class="audience-ring">
    <text class="ring-label"><textPath href="#arc-top" startOffset="209" textLength="799" lengthAdjust="spacingAndGlyphs">LOCAL + STATE GOVERNMENT</textPath></text>
    <text class="ring-label"><textPath href="#arc-top" startOffset="1100" textLength="1047" lengthAdjust="spacingAndGlyphs">SPORT + LEISURE FACILITY MANAGERS</textPath></text>
    <text class="ring-label"><textPath href="#arc-bottom" startOffset="174" textLength="1116" lengthAdjust="spacingAndGlyphs">INVESTORS, DEVELOPERS, ARCHITECTS + DESIGNERS</textPath></text>
    <text class="ring-label"><textPath href="#arc-bottom" startOffset="1398" textLength="1021" lengthAdjust="spacingAndGlyphs">SPORT RECREATION + COMMUNITY PROVIDERS</textPath></text>
    <circle class="ring-dot" cx="196" cy="783" r="13"/>
    <circle class="ring-dot" cx="833" cy="180" r="13"/>
    <circle class="ring-dot" cx="1737" cy="783" r="13"/>
    <circle class="ring-dot" cx="160" cy="1084" r="13"/>
    <circle class="ring-dot" cx="1013" cy="1787" r="13"/>
    <circle class="ring-dot" cx="1760" cy="1084" r="13"/>
  </g>

  <!-- Quadrants -->
  <g class="quadrants" clip-path="url(#disc)">
    <rect class="quadrant-planning" x="200" y="200" width="766" height="766" fill="var(--mid-blue)"/>
    <rect class="quadrant-management" x="966" y="200" width="766" height="766" fill="var(--navy)"/>
    <rect class="quadrant-participation" x="200" y="966" width="766" height="766" fill="var(--navy)"/>
    <rect class="quadrant-impact" x="966" y="966" width="766" height="766" fill="var(--mid-blue)"/>
    <path class="wave" d="M235,688 C330,690 430,740 510,820 C550,860 575,900 600,932 L200,932 L200,688 Z" fill="var(--light-blue)"/>
    <path class="wave" d="M1000,1292 C1150,1335 1290,1290 1420,1212 C1530,1145 1620,1100 1700,1062 L1732,1732 L1000,1732 Z" fill="var(--light-blue)"/>
    <rect class="divider" x="933" y="200" width="67" height="1532" fill="var(--bg)"/>
    <rect class="divider" x="200" y="932" width="1532" height="68" fill="var(--bg)"/>
  </g>

  <!-- Bubbles -->
  <g class="bubbles" fill="var(--light-blue)">
    <circle cx="412" cy="610" r="15"/><circle cx="387" cy="638" r="9"/><circle cx="425" cy="665" r="7"/>
    <circle cx="1478" cy="1082" r="17"/><circle cx="1522" cy="1117" r="11"/><circle cx="1484" cy="1131" r="6"/>
  </g>

  <!-- Hub -->
  <circle class="hub-ring" cx="966" cy="966" r="283" fill="var(--bg)"/>

  <!-- Stage tabs -->
  <g class="stage-tabs">
    <rect x="507" y="791" width="300" height="77" rx="38" fill="var(--bg)"/>
    <path d="M550,805 H778 L746,853 H550 Q527,853 527,829 Q527,805 550,805 Z" fill="var(--navy)"/>
    <text class="tab-text" x="596" y="837" textLength="83" lengthAdjust="spacingAndGlyphs">Planning</text>

    <rect x="1125" y="791" width="300" height="77" rx="38" fill="var(--bg)"/>
    <path d="M1155,806 H1378 Q1401,806 1401,829 Q1401,853 1378,853 H1186 Z" fill="var(--mid-blue)"/>
    <text class="tab-text" x="1219" y="837" textLength="131" lengthAdjust="spacingAndGlyphs">Management</text>

    <rect x="507" y="1055" width="300" height="77" rx="38" fill="var(--bg)"/>
    <path d="M550,1069 H745 L773,1118 H550 Q527,1118 527,1094 Q527,1069 550,1069 Z" fill="var(--mid-blue)"/>
    <text class="tab-text" x="532" y="1101" textLength="216" lengthAdjust="spacingAndGlyphs">Growing Participation</text>

    <rect x="1125" y="1055" width="300" height="77" rx="38" fill="var(--bg)"/>
    <path d="M1188,1069 H1378 Q1401,1069 1401,1092 Q1401,1117 1378,1117 H1160 Z" fill="var(--navy)"/>
    <text class="tab-text" x="1197" y="1092" textLength="191" lengthAdjust="spacingAndGlyphs">Community Impact</text>
    <text class="tab-text" x="1249" y="1112" textLength="124" lengthAdjust="spacingAndGlyphs">+ Outcomes</text>
  </g>

  <!-- Core -->
  <circle class="core" cx="966" cy="966" r="208" fill="var(--mid-blue)"/>
  <g class="core-text">
    <text x="812" y="912" textLength="305" lengthAdjust="spacingAndGlyphs">Community</text>
    <text x="966" y="958" text-anchor="middle">+</text>
    <text x="805" y="1008" textLength="320" lengthAdjust="spacingAndGlyphs">Stakeholder</text>
    <text x="797" y="1052" textLength="335" lengthAdjust="spacingAndGlyphs">Engagement</text>
  </g>

  <!-- Section pills -->
  <rect x="597" y="672" width="738" height="76" rx="30" fill="var(--white)"/>
  <text class="pill-text" x="614" y="718" textLength="702" lengthAdjust="spacingAndGlyphs">Community, aquatic + recreation facilities</text>
  <rect x="741" y="1197" width="450" height="77" rx="30" fill="var(--white)"/>
  <text class="pill-text" x="776" y="1246" textLength="379" lengthAdjust="spacingAndGlyphs">Community Activation</text>

  <!-- Planning services -->
  <g class="service-list">
    <text class="service-text" x="630" y="359" textLength="244" lengthAdjust="spacingAndGlyphs">Feasibility Studies</text>
    <text class="service-text" x="720" y="412" textLength="152" lengthAdjust="spacingAndGlyphs">Community</text>
    <text class="service-text" x="583" y="440" textLength="289" lengthAdjust="spacingAndGlyphs">Stakeholder Research</text>
    <text class="service-text" x="469" y="509" textLength="403" lengthAdjust="spacingAndGlyphs">Sport + Recreation Strategies</text>
    <text class="service-text" x="641" y="583" textLength="239" lengthAdjust="spacingAndGlyphs">Design Strategies</text>
    <text class="service-text" x="548" y="630" textLength="332" lengthAdjust="spacingAndGlyphs">Indoor + Outdoor Spaces</text>
    <g class="bullet"><circle cx="897" cy="352" r="7"/><circle cx="897" cy="414" r="7"/><circle cx="897" cy="497" r="7"/><circle cx="897" cy="572" r="7"/><circle cx="897" cy="620" r="7"/></g>
  </g>

  <!-- Management services -->
  <g class="service-list">
    <text class="service-text" x="1055" y="336" textLength="147" lengthAdjust="spacingAndGlyphs">Actuvating</text>
    <text class="service-text" x="1055" y="364" textLength="269" lengthAdjust="spacingAndGlyphs">underutilised assets</text>
    <text class="service-text" x="1055" y="412" textLength="238" lengthAdjust="spacingAndGlyphs">Income + Revenue</text>
    <text class="service-text" x="1055" y="440" textLength="297" lengthAdjust="spacingAndGlyphs">Generation Strategies</text>
    <text class="service-text" x="1058" y="500" textLength="376" lengthAdjust="spacingAndGlyphs">Mystery Shopper + Business</text>
    <text class="service-text" x="1058" y="528" textLength="175" lengthAdjust="spacingAndGlyphs">Health Check</text>
    <text class="service-text" x="1058" y="582" textLength="373" lengthAdjust="spacingAndGlyphs">Financial Funding Strategies</text>
    <text class="service-text" x="1057" y="631" textLength="233" lengthAdjust="spacingAndGlyphs">Business Planning</text>
    <g class="bullet"><circle cx="1032" cy="352" r="7"/><circle cx="1032" cy="414" r="7"/><circle cx="1032" cy="497" r="7"/><circle cx="1032" cy="572" r="7"/><circle cx="1032" cy="620" r="7"/></g>
  </g>

  <!-- Participation services -->
  <g class="service-list">
    <text class="service-text" x="678" y="1329" textLength="202" lengthAdjust="spacingAndGlyphs">Trends Insights</text>
    <text class="service-text" x="679" y="1375" textLength="198" lengthAdjust="spacingAndGlyphs">Health Profiling</text>
    <text class="service-text" x="425" y="1419" textLength="450" lengthAdjust="spacingAndGlyphs">Community Program Development</text>
    <text class="service-text" x="501" y="1460" textLength="379" lengthAdjust="spacingAndGlyphs">Phyisical Activity Strategies</text>
    <text class="service-text" x="520" y="1507" textLength="356" lengthAdjust="spacingAndGlyphs">Specific Cohort Strategies</text>
    <text class="service-text" x="660" y="1550" textLength="217" lengthAdjust="spacingAndGlyphs">Sport + Program</text>
    <text class="service-text" x="625" y="1578" textLength="252" lengthAdjust="spacingAndGlyphs">Specific Strategies</text>
    <g class="bullet"><circle cx="897" cy="1319" r="7"/><circle cx="897" cy="1368" r="7"/><circle cx="897" cy="1410" r="7"/><circle cx="897" cy="1451" r="7"/><circle cx="897" cy="1500" r="7"/><circle cx="897" cy="1553" r="7"/></g>
  </g>

  <!-- Impact services -->
  <g class="service-list">
    <text class="service-text" x="1053" y="1328" textLength="401" lengthAdjust="spacingAndGlyphs">Community Impact Monitoring</text>
    <text class="service-text" x="1055" y="1374" textLength="155" lengthAdjust="spacingAndGlyphs">Social Value</text>
    <text class="service-text" x="1057" y="1418" textLength="387" lengthAdjust="spacingAndGlyphs">Community Outcomes + KPIs</text>
    <text class="service-text" x="1055" y="1459" textLength="261" lengthAdjust="spacingAndGlyphs">Contact Monitoring</text>
    <g class="bullet"><circle cx="1032" cy="1319" r="7"/><circle cx="1032" cy="1368" r="7"/><circle cx="1032" cy="1410" r="7"/><circle cx="1032" cy="1451" r="7"/></g>
  </g>
</svg>
</body>
</html>
```